Business card for partnership

Plumbing and hvac company needing a minimal business card. We already have a logo i would like the front of the card just the logo and the back have all info.

Target Market(s)

Commercial facilities

Industry/Entity Type

Plumbing hvac

Contact Information for Business Card

We would like it double sided. Logo big and bold on the front and out info on the back. Our info on back would be name and position phone, email, and location

```html
<!DOCTYPE html>
<html lang="en">
<head>
<meta charset="utf-8">
<title>Kiln Mechanical – Business Card</title>
<link href="https://fonts.googleapis.com/css2?family=Montserrat:wght@400;500;600;700&display=swap" rel="stylesheet">
<style>
  :root {
    --canvas: #3a3a3a;
    --paper: #ffffff;
    --paper-shade: #f4f4f4;
    --ink: #2b2b2b;
    --charcoal: #333333;
    --orange: #f07a2a;
    --orange-deep: #e0562a;
    --orange-light: #f5a04e;
    --rule: #555555;
  }
  * { margin: 0; padding: 0; box-sizing: border-box; }
  html, body { width: 1200px; height: 1200px; overflow: hidden; }
  body {
    background: var(--canvas);
    font-family: "Montserrat", sans-serif;
    position: relative;
  }
  .card {
    position: absolute;
    left: 150px;
    width: 900px;
    height: 514px;
    border-radius: 36px;
    overflow: hidden;
  }
  .card--info { top: 60px; background: linear-gradient(180deg, var(--paper) 0%, var(--paper-shade) 100%); }
  .card--logo { top: 626px; background: var(--charcoal); }

  /* wordmark */
  .wordmark {
    position: absolute;
    display: flex;
    align-items: center;
    gap: 18px;
  }
  .wordmark__mark {
    width: 40px; height: 40px;
    background: var(--orange);
  }
  .wordmark__name {
    font-weight: 700;
    line-height: 0.95;
    letter-spacing: 2px;
    text-transform: uppercase;
  }
  .wordmark__name span { display: block; }
  .wordmark__top { font-size: 96px; }
  .wordmark__bottom { font-size: 46px; letter-spacing: 5px; margin-top: 8px; }

  .card--info .wordmark { left: 250px; top: 70px; }
  .card--info .wordmark__name { color: var(--ink); }
  .card--info .wordmark__top { font-size: 86px; }
  .card--info .wordmark__bottom { font-size: 40px; }

  .card--logo .wordmark { left: 160px; top: 140px; }
  .card--logo .wordmark__mark { width: 54px; height: 54px; }
  .card--logo .wordmark__name { color: var(--paper); }
  .card--logo .wordmark__top { font-size: 130px; }
  .card--logo .wordmark__bottom { font-size: 60px; letter-spacing: 7px; }

  /* person */
  .person {
    position: absolute;
    left: 60px;
    top: 360px;
    padding-left: 22px;
    border-left: 7px solid var(--orange);
  }
  .person__name {
    color: var(--orange);
    font-size: 46px;
    font-weight: 600;
    line-height: 1;
    letter-spacing: 1px;
  }
  .person__role {
    color: var(--ink);
    font-size: 20px;
    font-weight: 500;
    letter-spacing: 1px;
    margin-top: 6px;
  }

  .divider {
    position: absolute;
    left: 520px;
    top: 290px;
    width: 1px;
    height: 100px;
    background: var(--rule);
  }

  .contacts {
    position: absolute;
    left: 560px;
    top: 282px;
    list-style: none;
  }
  .contacts__item {
    display: flex;
    align-items: center;
    gap: 12px;
    color: var(--ink);
    font-size: 20px;
    height: 38px;
  }
  .contacts__icon { width: 22px; height: 22px; flex: none; }

  .base-band {
    position: absolute;
    left: 0; bottom: 0;
    width: 100%;
    height: 22px;
  }
</style>
</head>
<body>

  <section class="card card--info" aria-label="Card with contact details">
    <div class="wordmark">
      <div class="wordmark__mark"></div>
      <div class="wordmark__name"><span class="wordmark__top">Kiln</span><span class="wordmark__bottom">Mechanical</span></div>
    </div>

    <div class="divider"></div>

    <ul class="contacts">
      <li class="contacts__item">
        <svg class="contacts__icon" viewBox="0 0 24 24"><path fill="#f07a2a" d="M6.6 10.8c1.4 2.8 3.8 5.1 6.6 6.6l2.2-2.2c.3-.3.7-.4 1-.2 1.1.4 2.3.6 3.6.6.6 0 1 .4 1 1V20c0 .6-.4 1-1 1C10.6 21 3 13.4 3 4c0-.6.4-1 1-1h3.5c.6 0 1 .4 1 1 0 1.3.2 2.5.6 3.6.1.3 0 .7-.2 1z"/></svg>
        (000) 000 0000
      </li>
      <li class="contacts__item">
        <svg class="contacts__icon" viewBox="0 0 24 24"><rect x="2" y="5" width="20" height="14" fill="#f07a2a"/><path d="M2 5l10 8 10-8" fill="none" stroke="#fff" stroke-width="1.6"/></svg>
        email@youremail.com
      </li>
      <li class="contacts__item">
        <svg class="contacts__icon" viewBox="0 0 24 24" fill="none" stroke="#f07a2a" stroke-width="1.8"><circle cx="12" cy="12" r="9.5"/><ellipse cx="12" cy="12" rx="4.2" ry="9.5"/><path d="M2.5 12h19M4 7h16M4 17h16"/></svg>
        www.yourwebsite.com
      </li>
    </ul>

    <div class="person">
      <div class="person__name">JOHN DOE</div>
      <div class="person__role">POSITION</div>
    </div>

    <svg class="base-band" viewBox="0 0 900 22" preserveAspectRatio="none">
      <defs>
        <linearGradient id="bandGlow" x1="0" x2="1" y1="0" y2="0">
          <stop offset="0" stop-color="#e0562a"/>
          <stop offset="1" stop-color="#f5a04e"/>
        </linearGradient>
      </defs>
      <polygon points="0,22 0,10 566,0 566,22" fill="url(#bandGlow)"/>
      <polygon points="574,22 574,0 900,0 900,22" fill="#333333"/>
    </svg>
  </section>

  <section class="card card--logo" aria-label="Card with company name">
    <div class="wordmark">
      <div class="wordmark__mark"></div>
      <div class="wordmark__name"><span class="wordmark__top">Kiln</span><span class="wordmark__bottom">Mechanical</span></div>
    </div>
  </section>

</body>
</html>
```